Clean professional design needed for landscape property business

We need a logo for a new lawncare, landscaping , property maintenance business called Meadow Trim.
Our services include lawn mowing, garden maintenance, clean ups and some property maintenance.
We want a double sided business card that is clean and very professional using the colour scheme from our logo which is provided.
the business card should have impact as we will use these to drop into people's letterboxes as a marketing drop.
Initially we want to see what you come up with so there is a very wide scope here to work with.
Updates

Project Deadline Extended
Reason: we feel our original deadline was too short. we have extended to give more time for quality submissions.

Target Market(s)

High end property owners who don't wish to do there own gardneing or property maintenance

Industry/Entity Type

Business

Contact Information for Business Card

Name
Postion/ Title
Phone number
mobile
web address
physical address

services offered

Font styles to use
Sans Serif

Requirements
Must have
• curved edges preferrred
Nice to have
• We like the idea of the logo being embossed or etched into the card so it looks like it is below the surface of the card
Should not have
• No stock images or characters.

```html
<!DOCTYPE html>
<html lang="en">
<head>
<meta charset="utf-8">
<title>Meadow Trim Business Card</title>
<link href="https://fonts.googleapis.com/css2?family=Open+Sans:wght@400;600;700&display=swap" rel="stylesheet">
<style>
  :root {
    --bg: #ecebe8;
    --charcoal: #4a4a4a;
    --green: #7cc242;
    --green-soft: #8fcf55;
    --grey-mark: #8a8a8a;
    --ink: #3a3a3a;
    --paper: #ffffff;
    --rule: #4d8a22;
  }
  * { margin: 0; padding: 0; box-sizing: border-box; }
  html, body { width: 1200px; height: 800px; overflow: hidden; }
  body {
    background: var(--bg);
    font-family: "Open Sans", sans-serif;
    display: flex;
    align-items: center;
    justify-content: center;
    gap: 60px;
  }
  .card {
    width: 520px;
    height: 318px;
    border-radius: 26px;
    position: relative;
    overflow: hidden;
    box-shadow: 0 6px 18px rgba(0,0,0,0.18);
  }

  /* Back side */
  .card--back { background: var(--charcoal); }
  .card--back .brand {
    position: absolute;
    left: 70px;
    top: 92px;
  }
  .brand-name {
    font-weight: 700;
    font-size: 62px;
    letter-spacing: -2px;
    line-height: 1;
    color: var(--green);
    display: flex;
    align-items: center;
    gap: 14px;
    white-space: nowrap;
  }
  .brand-square {
    width: 16px; height: 16px;
    background: var(--paper);
    display: inline-block;
  }
  .brand-tagline {
    font-weight: 600;
    font-size: 15px;
    letter-spacing: 15px;
    color: var(--green);
    margin-top: 10px;
    padding-left: 4px;
    white-space: nowrap;
  }
  .services {
    position: absolute;
    left: 0; right: 0;
    bottom: 46px;
    text-align: center;
    color: var(--paper);
    font-weight: 600;
    font-size: 13.5px;
    white-space: nowrap;
  }

  /* Front side */
  .card--front { background: var(--paper); }
  .feature-shape {
    position: absolute;
    left: -70px;
    top: 40px;
    width: 250px;
    height: 250px;
  }
  .feature-square {
    position: absolute;
    left: 30px;
    bottom: 22px;
    width: 52px; height: 52px;
    background: var(--grey-mark);
  }
  .front-brand {
    position: absolute;
    left: 212px;
    top: 34px;
  }
  .front-brand .brand-name { font-size: 36px; letter-spacing: -1px; gap: 8px; }
  .front-brand .brand-square { width: 10px; height: 10px; background: var(--ink); }
  .front-brand .brand-tagline { font-size: 9px; letter-spacing: 8px; margin-top: 5px; }
  .person {
    position: absolute;
    left: 212px;
    top: 146px;
    font-size: 25px;
    color: var(--ink);
    font-weight: 400;
    white-space: nowrap;
  }
  .person strong { font-weight: 700; }
  .rule {
    position: absolute;
    left: 212px; right: 24px;
    top: 186px;
    height: 2px;
    background: var(--rule);
  }
  .contacts {
    position: absolute;
    left: 212px; right: 24px;
    top: 204px;
    display: grid;
    grid-template-columns: max-content max-content;
    justify-content: space-between;
    row-gap: 10px;
    font-size: 11.5px;
    color: var(--ink);
    list-style: none;
  }
  .contacts li { display: flex; align-items: center; gap: 6px; white-space: nowrap; }
  .contacts svg { width: 11px; height: 11px; flex: none; }
</style>
</head>
<body>

  <section class="card card--back" aria-label="Card back">
    <div class="brand">
      <div class="brand-name">meadowtrim <span class="brand-square"></span></div>
      <div class="brand-tagline">LAWN AND GARDENS</div>
    </div>
    <p class="services">Lawn Mowing | Garden Maintenance | Wholesale Plants | Clean ups</p>
  </section>

  <section class="card card--front" aria-label="Card front">
    <svg class="feature-shape" viewBox="0 0 250 250" aria-hidden="true">
      <circle cx="125" cy="125" r="125" fill="var(--green-soft)"/>
    </svg>
    <div class="feature-square" aria-hidden="true"></div>

    <div class="front-brand">
      <div class="brand-name">meadowtrim <span class="brand-square"></span></div>
      <div class="brand-tagline">LAWN AND GARDENS</div>
    </div>

    <h1 class="person">Colin <strong>Mercer</strong></h1>
    <div class="rule"></div>

    <ul class="contacts">
      <li>
        <svg viewBox="0 0 12 12"><path d="M2 1h3l1 3-1.5 1a6 6 0 0 0 2.5 2.5L8 6l3 1v3c0 .6-.4 1-1 1A9 9 0 0 1 1 2c0-.6.4-1 1-1z" fill="var(--rule)"/></svg>
        (02) 8000 4217 3
      </li>
      <li>
        <svg viewBox="0 0 12 12"><rect x="0.5" y="2" width="11" height="8" fill="var(--rule)"/><path d="M0.5 2l5.5 4.5L11.5 2" stroke="#fff" fill="none"/></svg>
        colin@meadowtrim.sydney
      </li>
      <li>
        <svg viewBox="0 0 12 12"><rect x="3" y="0.5" width="6" height="11" rx="1" fill="none" stroke="var(--rule)"/></svg>
        0400 718 293
      </li>
      <li>
        <svg viewBox="0 0 12 12"><circle cx="6" cy="6" r="5.2" fill="var(--rule)"/><path d="M1 6h10M6 1v10" stroke="#fff" stroke-width="0.8"/></svg>
        www.meadowtrim.sydney
      </li>
    </ul>
  </section>

</body>
</html>
```